Business Card Design for Event Planning Company

Create a business card for event planning company using our new logo. After I pick the design, I will need files made for 6 employees. Our company provides event design & logistics services as well as venue management. The font should be sans serif and complementary to the logo. I will need to know the name of the font selected for the final design. The phone numbers listed should be separated by "." not "-"

Address for the card
PO Box 318, Washington, DC 20019

Card One
Lorna Pettibone
lpettibone@galavoyant.com
202.481.7730

Card Two
Miriam Okonkwo
mokonkwo@galavoyant.com
202.556.2047

Card Three
Tessa Varnholt
tvarnholt@galavoyant.com
978.620.4471

Card Four
Robin Fess
rfess@galavoyant.com
202.718.3362

Card Five
Ada-Rose Pelletan-Uzor
adarose@galavoyant.com
202.839.1205

Card Six
Beatrix Holloway
Beatrix@galavoyant.com
202.492.6618

Target Market(s)

Corporate/Non-Profit

Industry/Entity Type

Event Planning

Contact Information for Business Card

Address for the card

Card One
Lorna Pettibone
lpettibone@galavoyant.com
202.481.7730

Card Two
Miriam Okonkwo
202.556.2047

Card Three
Tessa Varnholt
978.620.4471

Card Four
Robin Fess
rfess@galavoyant.com
202.718.3362

Card Five
Ada-Rose Pelletan-Uzor
202.839.1205

Card Six
Beatrix Holloway
202.492.6618

Font styles to use
Sans Serif

Colors

Designer to choose colors to be used in the design.

Requirements
Must have
• Two-sided with logo
Should not have
• Extra colors or be too busy

```html
<!DOCTYPE html>
<html lang="en">
<head>
<meta charset="utf-8">
<title>Galavoyant Business Card</title>
<link href="https://fonts.googleapis.com/css2?family=Lato:wght@300;400;700&display=swap" rel="stylesheet">
<style>
  :root {
    --teal: #4c9c96;
    --ink: #25282a;
    --card: #ffffff;
    --card-back: #f4f5f5;
    --backdrop: #dfe3e4;
  }
  * { box-sizing: border-box; margin: 0; padding: 0; }
  html, body {
    width: 1200px; height: 900px; overflow: hidden;
    background: var(--backdrop);
    font-family: "Lato", Arial, sans-serif;
    color: var(--ink);
  }
  .sheet {
    width: 1200px; height: 900px;
    display: flex; flex-direction: column;
    align-items: center; justify-content: center; gap: 44px;
  }
  .card {
    position: relative;
    width: 700px; height: 400px;
    border-radius: 18px;
    background: var(--card);
    box-shadow: 0 6px 18px rgba(0,0,0,0.12);
    overflow: hidden;
  }
  .card--back { background: linear-gradient(135deg, var(--card-back), #ffffff 70%); }

  .wordmark {
    display: flex; align-items: center; gap: 14px;
    font-weight: 300; color: var(--teal); letter-spacing: 1px;
  }
  .wordmark__dot {
    width: 0.62em; height: 0.62em; border-radius: 50%;
    background: var(--teal);
  }
  .card--front .wordmark {
    position: absolute; left: 50%; top: 50%;
    transform: translate(-50%, -50%);
    font-size: 68px;
  }
  .card--back .wordmark {
    position: absolute; right: 70px; top: 210px;
    font-size: 40px;
  }

  .name-tab {
    position: absolute; left: 0; top: 26px;
    width: 290px; height: 56px;
  }
  .name-tab svg { position: absolute; inset: 0; }
  .name-tab__label {
    position: absolute; left: 30px; top: 0; height: 56px;
    display: flex; align-items: center; gap: 12px;
    color: #fff; font-size: 21px; font-weight: 400;
  }

  .contact-list {
    position: absolute; left: 34px; top: 122px;
    list-style: none;
    display: flex; flex-direction: column; gap: 18px;
  }
  .contact-list li {
    display: flex; align-items: center; gap: 14px;
    font-size: 15px; color: var(--ink);
  }
  .icon-box {
    width: 28px; height: 28px; border-radius: 6px;
    background: var(--teal);
    display: flex; align-items: center; justify-content: center;
  }
</style>
</head>
<body>
<main class="sheet">

  <section class="card card--front" aria-label="Card front">
    <div class="wordmark"><span class="wordmark__dot"></span><span>galavoyant</span></div>
  </section>

  <section class="card card--back" aria-label="Card back">
    <div class="name-tab">
      <svg width="290" height="56" viewBox="0 0 290 56">
        <path d="M0 0 H290 L262 48 Q258 56 248 56 H0 Z" fill="var(--teal)"/>
      </svg>
      <div class="name-tab__label">
        <svg width="22" height="22" viewBox="0 0 22 22">
          <rect x="1" y="1" width="20" height="20" rx="4" fill="#fff"/>
          <circle cx="11" cy="8.5" r="3.6" fill="var(--teal)"/>
          <path d="M4.5 18 Q11 10.5 17.5 18 Z" fill="var(--teal)"/>
        </svg>
        <span class="name-tab__text">Lorna Pettibone</span>
      </div>
    </div>

    <ul class="contact-list">
      <li>
        <span class="icon-box">
          <svg width="16" height="16" viewBox="0 0 16 16"><path d="M3.5 1.5 L6 1.5 L7 5 L5.3 6.3 Q6.6 9.4 9.7 10.7 L11 9 L14.5 10 L14.5 12.5 Q14.5 14.5 12.5 14.5 Q1.5 13.5 1.5 3.5 Q1.5 1.5 3.5 1.5 Z" fill="#fff"/></svg>
        </span>
        <span>202.481.7730</span>
      </li>
      <li>
        <span class="icon-box">
          <svg width="16" height="16" viewBox="0 0 16 16" fill="none" stroke="#fff" stroke-width="1.8" stroke-linecap="round"><path d="M6.5 9.5 L9.5 6.5"/><path d="M7.5 4.5 L9 3 A2.8 2.8 0 0 1 13 7 L11.5 8.5"/><path d="M8.5 11.5 L7 13 A2.8 2.8 0 0 1 3 9 L4.5 7.5"/></svg>
        </span>
        <span>lpettibone@galavoyant.com</span>
      </li>
      <li>
        <span class="icon-box">
          <svg width="16" height="16" viewBox="0 0 16 16"><path d="M8 15 Q2.5 9 2.5 6 A5.5 5.5 0 0 1 13.5 6 Q13.5 9 8 15 Z" fill="#fff"/><circle cx="8" cy="6" r="2" fill="var(--teal)"/></svg>
        </span>
        <span>PO Box 318, Washington, DC 20019</span>
      </li>
    </ul>

    <div class="wordmark"><span class="wordmark__dot"></span><span>galavoyant</span></div>
  </section>

</main>
</body>
</html>
```